TrueGrindz Complete Stationery - Logo already designed

I already have the logo designed see attached. I need have a full set of stationary and business card designed for printing. I have attached an example of what I mean.

Please feel free to be creative. Also you can use the X in the logo by its self if you think it will work.

My details:

Name: Corwin Lestak
Social media handles: @corwinlestak
W: corwinlestak.com
E: info@corwinlestak.com
​P: 08 7493 5286
PO Box 7382, Marrowvale 6087
ABN 83 402 719 265

Target Market(s)

Anyone looking to be inspired.

Industry/Entity Type

Business

Font styles to use
Sans Serif

Colors
fbee3e
000000

Requirements
Must have
• My details:
• Name: Corwin Lestak
• Social media handles: @corwinlestak
• W: corwinlestak.com
• E: info@corwinlestak.com
• ​P: 08 7493 5286
• PO Box 7382, Marrowvale 6087
• ABN 83 402 719 265
Nice to have
• Something a little different
Should not have
• must not look tacky.

```html
<!DOCTYPE html>
<html lang="en">
<head>
<meta charset="utf-8">
<title>TrueGrindz Business Card</title>
<link rel="stylesheet" href="https://fonts.googleapis.com/css2?family=Oswald:wght@700&family=Open+Sans:wght@400;600&display=swap">
<style>
  :root {
    --backdrop: #8c8c8c;
    --paper: #ececec;
    --brand-yellow: #d8ae00;
    --ink: #231f20;
    --text-grey: #555559;
    --rule-grey: #a9a9a9;
  }
  * { margin: 0; padding: 0; box-sizing: border-box; }
  html, body {
    width: 1105px; height: 1200px; overflow: hidden;
    background: var(--backdrop);
    font-family: "Open Sans", Arial, sans-serif;
  }
  .canvas { position: relative; width: 1105px; height: 1200px; }
  .card { position: absolute; left: 182px; width: 746px; height: 424px; overflow: hidden; }
  .card-front { top: 119px; background: var(--paper); }
  .card-back { top: 637px; background: var(--brand-yellow); }

  .brand-name {
    position: absolute; left: 84px; top: 168px;
    font-family: "Oswald", "Arial Narrow", sans-serif; font-weight: 700;
    font-size: 62px; line-height: 72px; color: var(--ink); letter-spacing: 0.5px;
  }
  .divider { position: absolute; left: 395px; top: 91px; width: 1px; height: 204px; background: var(--rule-grey); }
  .contact { position: absolute; left: 426px; top: 90px; color: var(--text-grey); font-size: 19px; line-height: 27px; }
  .contact-name { color: var(--brand-yellow); font-size: 27px; font-weight: 600; line-height: 36px; margin-bottom: 22px; letter-spacing: 0.3px; }
  .contact-line { display: flex; align-items: center; gap: 9px; }
  .contact-line svg { width: 15px; height: 15px; fill: var(--brand-yellow); flex: none; }
  .address { margin-bottom: 10px; }
  .abn { margin-top: 7px; }

  .base-band { position: absolute; left: 0; bottom: 0; width: 100%; height: 11px; background: var(--ink); }
  .web-tab { position: absolute; right: 0; bottom: 0; width: 360px; height: 44px; }
  .web-tab svg { position: absolute; inset: 0; }
  .web-address {
    position: absolute; right: 30px; bottom: 8px;
    font-size: 19px; letter-spacing: 2.4px; color: var(--ink);
  }

  .social { position: absolute; left: 72px; top: 326px; }
  .social-dots { display: flex; gap: 6px; margin-left: 2px; }
  .social-dots span { width: 37px; height: 37px; border-radius: 50%; background: var(--paper); opacity: 0.9; }
  .handle { margin-top: 4px; color: var(--paper); font-size: 19px; }
  .back-name {
    position: absolute; right: 34px; top: 268px;
    font-family: "Oswald", "Arial Narrow", sans-serif; font-weight: 700;
    font-size: 54px; line-height: 70px; color: var(--paper);
  }
</style>
</head>
<body>
<main class="canvas">
  <section class="card card-front">
    <div class="brand-name">TrueGrindz</div>
    <div class="divider"></div>
    <div class="contact">
      <div class="contact-name">CORWIN LESTAK</div>
      <div class="address">PO Box 7382<br>Marrowvale 6087</div>
      <div class="contact-line">
        <svg viewBox="0 0 16 16" aria-hidden="true"><path d="M3.5 1l2.6 3.1-1.5 1.7c.9 2 2.6 3.7 4.6 4.6l1.7-1.5L14 11.5 12.6 14C6.5 14 2 9.5 2 3.4z"/></svg>
        <span>08 7493 5286</span>
      </div>
      <div class="contact-line">
        <svg viewBox="0 0 16 16" aria-hidden="true"><path d="M1 3h14v1.2L8 9 1 4.2z M1 6l7 4.8L15 6v7H1z"/></svg>
        <span>info@corwinlestak.com</span>
      </div>
      <div class="abn">ABN 83 402 719 265</div>
    </div>
    <div class="base-band"></div>
    <div class="web-tab">
      <svg viewBox="0 0 360 44" width="360" height="44" preserveAspectRatio="none" aria-hidden="true">
        <polygon points="30,0 360,0 360,44 0,44" fill="var(--brand-yellow)"/>
      </svg>
      <span class="web-address">www.corwinlestak.com</span>
    </div>
  </section>

  <section class="card card-back">
    <div class="social">
      <div class="social-dots"><span></span><span></span><span></span></div>
      <div class="handle">@corwinlestak</div>
    </div>
    <div class="back-name">TrueGrindz</div>
  </section>
</main>
</body>
</html>
```